FACEBOOK PAGE FOR BREVLO PLUMBING GROUP

We need a facebook banner for our new plumbing business.

Needs to be catchy and inline with our logo.

Phone: 0472 836 291
Email: hello@brevlo.com.au
website: www.brevlo.com.au
Servicing: Perth Metro Areas and surrounding suburbs
Services:
*We offer a wide range of services, including:
Plumbing – General maintenance, blocked drains, toilet repairs, burst pipes, reticulation, renovations & emergencies.

*Hot Water – Installation, servicing & repairs for all systems.

*Cooling & Heating – Air conditioning, evaporative cooling & heater servicing.

*Filtration – Filtered taps, under-sink systems & whole-house filtration setups.

Our Mission

Brevlo Group believes plumbing shouldn't break the bank - or your trust. Our mission is to provide honest, affordable, and no-nonsense plumbing services that get the job done right the first time. No runaround - just reliable work, and the respect every customer deserves.

What Makes Us Different???

Upfront Fixed Pricing
No surprises, no hidden fees. You get clear, honest quotes before any work begins.

Respectful, Customer-First Service
We show up on time, communicate clearly, and treat your property like it’s our own.

Locals Serving Locals
We’re proud to support the Perth community with reliable, high-quality plumbing backed by real local care.

FOR THE DESIGNER A little background on us as a new biz for your reference:
By Locals, For Locals
After 13 years in the plumbing industry, seasoned local plumber Wade founded his company to address the widespread issue of homeowners and businesses being overcharged or receiving inferior work. He knew there had to be a better way—and that’s when Brevlo was created.
Today, Brevlo Group is a trusted plumbing company based in Osborne Park, proudly serving residential, commercial, and industrial clients across the Perth metro area. With over a decade of experience, we deliver expert workmanship, fair pricing, and treat every job—big or small—with the same care and professionalism.
Need it done right—and affordably? Get it sorted with BREVLO now!

```html
<!DOCTYPE html>
<html lang="en">
<head>
<meta charset="utf-8">
<title>Brevlo Plumbing Group – Facebook Banner</title>
<link href="https://fonts.googleapis.com/css2?family=Outfit:wght@300;400;500;600&display=swap" rel="stylesheet">
<style>
  :root{
    --stage:#383837;
    --paper:#ffffff;
    --navy:#27235c;
    --deep-blue:#0d4f96;
    --bright-blue:#0a8fd6;
    --sky:#19a6e3;
    --line-blue:#1d4e86;
    --lilac:#b3aac9;
    --lilac-light:#f4f2f8;
    --ink:#1f1c3e;
  }
  html,body{margin:0;padding:0;width:1200px;height:762px;overflow:hidden;background:var(--stage);font-family:"Outfit",sans-serif;}
  .banner{position:absolute;left:148px;top:124px;width:913px;height:515px;background:var(--paper);overflow:hidden;color:var(--ink);}
  .shapes{position:absolute;inset:0;}
  .intro{position:absolute;left:31px;top:26px;color:#fff;}
  .intro h2{margin:0;font-weight:400;font-size:23px;line-height:1;display:flex;align-items:center;gap:4px;}
  .intro h2::before{content:"";width:7px;height:7px;background:#fff;transform:rotate(45deg);display:inline-block;margin:0 3px 0 2px;}
  .mission-quote{margin:4px 0 6px;font-size:12.6px;line-height:16.5px;font-weight:300;width:440px;}
  .diff-list{list-style:none;margin:5px 0 0;padding:0;}
  .diff-list li{position:relative;padding-left:18px;font-size:11px;line-height:14px;font-weight:300;margin-bottom:5px;}
  .diff-list li svg{position:absolute;left:0;top:7px;width:11px;height:11px;}
  .brand{position:absolute;left:544px;top:52px;width:340px;display:flex;align-items:center;justify-content:center;gap:12px;}
  .brand-dot{width:34px;height:34px;border-radius:50%;background:var(--bright-blue);}
  .brand-name{font-size:58px;font-weight:600;letter-spacing:10px;color:var(--navy);line-height:1;}
  .area-pill{position:absolute;left:246px;top:236px;width:448px;height:25px;border-radius:9px;background:linear-gradient(90deg,var(--sky),var(--deep-blue) 60%,var(--navy));color:#fff;font-size:19px;font-weight:300;text-align:center;line-height:25px;box-shadow:2px 1px 2px rgba(0,0,0,.35);}
  .service{position:absolute;}
  .service h3{margin:0;font-weight:400;font-size:27px;line-height:1;color:var(--navy);}
  .service p{margin:4px 0 0;font-size:9.4px;line-height:11.8px;font-weight:400;}
  .service.right{text-align:right;}
  .contact{position:absolute;left:423px;top:422px;font-size:12.6px;line-height:21px;}
  .contact div{display:flex;align-items:center;gap:4px;}
  .contact svg{width:14px;height:14px;}
  .contact .phone{font-weight:600;}
</style>
</head>
<body>
<main class="banner">
  <svg class="shapes" viewBox="0 0 913 515" aria-hidden="true">
    <defs>
      <linearGradient id="panelFill" x1="0" y1="0" x2="1" y2="0">
        <stop offset="0" stop-color="#0b6db3"/>
        <stop offset="0.4" stop-color="#1a3f85"/>
        <stop offset="0.6" stop-color="#29235f"/>
      </linearGradient>
      <radialGradient id="badgeFill" cx="0.5" cy="0.5" r="0.5">
        <stop offset="0" stop-color="var(--lilac-light)"/>
        <stop offset="0.45" stop-color="#e6e2ef"/>
        <stop offset="1" stop-color="var(--lilac)"/>
      </radialGradient>
    </defs>
    <!-- header panel -->
    <path d="M0 0 H512 C506 120 468 200 338 218 C230 230 100 220 0 226 Z" fill="#1c9ad8"/>
    <path d="M0 0 H507 C500 118 460 192 330 211 C230 223 100 215 0 218 Z" fill="url(#panelFill)"/>
    <!-- service frames -->
    <g fill="none" stroke="var(--line-blue)" stroke-width="1.6">
      <path d="M413 268 H72 A40.5 40.5 0 0 0 72 349 H413"/>
      <path d="M413 387 H72 A41 41 0 0 0 72 469 H413"/>
      <path d="M554 268 H841 A40.5 40.5 0 0 1 841 349 H554"/>
      <path d="M554 387 H841 A41 41 0 0 1 841 469 H554"/>
    </g>
    <circle cx="131" cy="308" r="55" fill="url(#badgeFill)"/>
    <circle cx="131" cy="429" r="55" fill="url(#badgeFill)"/>
    <circle cx="782" cy="306" r="55" fill="url(#badgeFill)"/>
    <circle cx="782" cy="428" r="55" fill="url(#badgeFill)"/>
    <!-- icons -->
    <g fill="none" stroke="var(--navy)" stroke-width="2" stroke-linecap="round" stroke-linejoin="round">
      <!-- tap -->
      <path d="M120 296 h14 v-8 h6 v16 h-6 v-6 h-10 q-6 0 -6 6 v10 h-6 v-10 q0 -12 12 -12 z"/>
      <path d="M137 288 v-6 M131 281 h12"/>
      <!-- water heater -->
      <rect x="108" y="402" width="41" height="46" rx="4"/>
      <path d="M118 430 q10 -10 20 0 M114 448 v8 h6 v-8 M137 448 v8 h6 v-8"/>
      <!-- hot water unit -->
      <rect x="755" y="300" width="54" height="29" rx="3"/>
      <path d="M761 306 h42 M794 300 v-14 M785 314 h18 M785 320 h18"/>
      <circle cx="768" cy="318" r="4"/>
      <!-- faucet -->
      <path d="M760 452 v-42 h16 v6 h-10 v6 h18 q16 0 16 14 h-8 q0 -6 -8 -6 h-18 v22 z"/>
      <path d="M798 440 q3 4 0 8 q-3 4 0 8 M803 440 q3 4 0 8 q-3 4 0 8"/>
    </g>
    <circle cx="794" cy="285" r="2.5" fill="var(--navy)"/>
    <path d="M114 318 q-6 9 0 12 q6 -3 0 -12z" fill="none" stroke="#3a8fd0" stroke-width="1.4"/>
    <path d="M130 425 q-4 6 0 8 q4 -2 0 -8z" fill="var(--navy)"/>
  </svg>

  <section class="intro">
    <h2>Our Mission</h2>
    <p class="mission-quote">"Plumbing shouldn't break the bank — or your trust. We provide honest, affordable, no-nonsense services that get it right the first time."</p>
    <h2>What Makes Us Different</h2>
    <ul class="diff-list">
      <li><svg viewBox="0 0 12 12"><circle cx="6" cy="6" r="5" fill="none" stroke="#fff"/><path d="M3.5 6 l2 2 l4 -5" fill="none" stroke="#fff"/></svg>Upfront Fixed Pricing<br>No hidden fees. Know your cost before we start.</li>
      <li><svg viewBox="0 0 12 12"><circle cx="6" cy="6" r="5" fill="none" stroke="#fff"/><path d="M3.5 6 l2 2 l4 -5" fill="none" stroke="#fff"/></svg>Respectful, Customer-First Service<br>We show up on time &amp; treat your space like our own.</li>
      <li><svg viewBox="0 0 12 12"><circle cx="6" cy="6" r="5" fill="none" stroke="#fff"/><path d="M3.5 6 l2 2 l4 -5" fill="none" stroke="#fff"/></svg>Locals Serving Locals<br>Proudly Perth-based — real service from real locals.</li>
    </ul>
  </section>

  <div class="brand"><span class="brand-name">BREVLO</span><span class="brand-dot"></span></div>

  <div class="area-pill">Perth Metro Areas and surrounding suburbs</div>

  <section class="service" style="left:198px;top:276px;">
    <h3>Plumbing</h3>
    <p>General maintenance, blocked drains,<br>toilet repairs, burst pipes, reticulation,<br>renovations &amp; emergencies.</p>
  </section>
  <section class="service" style="left:198px;top:402px;">
    <h3>Cooling &amp; Heating</h3>
    <p>Air conditioning, evaporative<br>cooling &amp; heater servicing.</p>
  </section>
  <section class="service right" style="right:206px;top:281px;">
    <h3>Hot Water</h3>
    <p>Installation, servicing &amp; repairs<br>for all systems.</p>
  </section>
  <section class="service right" style="right:206px;top:399px;">
    <h3>Filtration</h3>
    <p>Filtered taps, under-sink systems &amp;<br>whole-house filtration setups.</p>
  </section>

  <address class="contact" style="font-style:normal;">
    <div class="phone"><svg viewBox="0 0 14 14"><circle cx="7" cy="7" r="7" fill="var(--line-blue)"/><path d="M4.5 4 q0 5 5 6 l1-1.5 -1.7-1 -.8.8 q-1.6-.8-2.2-2.3 l.8-.8 -1-1.7z" fill="#fff"/></svg>0472 836 291</div>
    <div><svg viewBox="0 0 14 14"><circle cx="7" cy="7" r="7" fill="var(--line-blue)"/><g fill="none" stroke="#fff" stroke-width=".8"><circle cx="7" cy="7" r="4.5"/><ellipse cx="7" cy="7" rx="2" ry="4.5"/><path d="M2.5 7h9M3.3 4.7h7.4M3.3 9.3h7.4"/></g></svg>www.brevlo.com.au</div>
    <div><svg viewBox="0 0 14 14"><circle cx="7" cy="7" r="7" fill="var(--line-blue)"/><rect x="3.5" y="4.5" width="7" height="5" fill="none" stroke="#fff" stroke-width=".9"/><path d="M3.5 4.5 l3.5 3 l3.5 -3" fill="none" stroke="#fff" stroke-width=".9"/></svg>hello@brevlo.com.au</div>
  </address>
</main>
</body>
</html>
```